Real eatate

My company name is “Maple Crest Realestate” i would like to create a business card. I would like something modern and sleek similar to picture uploaded. All text in the business card should be black and the logo gold any shade.

```html
<!DOCTYPE html>
<html lang="en">
<head>
<meta charset="utf-8">
<title>Maple Crest Realestate – Business Card</title>
<link rel="stylesheet" href="https://fonts.googleapis.com/css2?family=Cinzel:wght@400&family=Roboto:wght@400;700&display=swap">
<style>
  :root {
    --backdrop: #d1d2d4;
    --card-white: #ffffff;
    --ink: #111111;
    --black: #000000;
    --charcoal: #4a4a4a;
    --gold: #d4a33a;
    --gold-light: #f6e55e;
    --gold-deep: #b8672e;
  }
  * { margin: 0; padding: 0; box-sizing: border-box; }
  html, body {
    width: 962px; height: 1200px; overflow: hidden;
    background: var(--backdrop);
  }
  .canvas { position: relative; width: 962px; height: 1200px; }

  .card {
    position: absolute; left: 30px; width: 905px; height: 543px;
    overflow: hidden;
  }
  .card--front { top: 40px; background: var(--card-white); }
  .card--back {
    top: 617px;
    background: radial-gradient(ellipse 90% 120% at 0% 0%, var(--charcoal) 0%, #141414 45%, var(--black) 75%);
  }
  .card__art { position: absolute; inset: 0; width: 100%; height: 100%; }

  .brand {
    position: absolute; display: flex; align-items: center;
    font-family: "Cinzel", serif; font-weight: 400; color: var(--gold);
  }
  .brand__dot { border-radius: 50%; background: var(--gold); flex: none; }
  .brand--front { left: 62px; top: 72px; gap: 38px; }
  .brand--front .brand__dot { width: 150px; height: 150px; }
  .brand--front .brand__name { font-size: 38px; line-height: 47px; }
  .brand--back { right: 70px; top: 170px; gap: 32px; }
  .brand--back .brand__dot { width: 180px; height: 180px; }
  .brand--back .brand__name { font-size: 44px; line-height: 56px; }

  .person {
    position: absolute; right: 60px; top: 276px; text-align: right;
    font-family: "Roboto", sans-serif; color: var(--ink);
  }
  .person__name { font-size: 38px; font-weight: 700; line-height: 46px; }
  .person__title { font-size: 26px; font-weight: 400; line-height: 32px; letter-spacing: 0.5px; }

  .contact {
    position: absolute; left: 62px; top: 389px; list-style: none;
    font-family: "Roboto", sans-serif; font-size: 21px; color: var(--ink);
  }
  .contact__item { display: flex; align-items: center; gap: 12px; height: 34px; letter-spacing: 0.5px; }
  .contact__icon { width: 24px; height: 24px; flex: none; }

  .address {
    position: absolute; left: 484px; top: 391px; height: 85px;
    display: flex; align-items: center;
    font-family: "Roboto", sans-serif; font-size: 21px; color: var(--ink);
  }
  .address__icon { width: 47px; height: 46px; }
  .address__rule {
    width: 2px; height: 85px; margin: 0 17px 0 17px;
    background: linear-gradient(var(--gold-light), var(--gold), var(--gold-deep));
  }
  .address__lines p { line-height: 36px; letter-spacing: 0.5px; }
</style>
</head>
<body>
<main class="canvas">

  <section class="card card--front" aria-label="Business card front">
    <svg class="card__art" viewBox="0 0 905 543" aria-hidden="true">
      <defs>
        <linearGradient id="header-shade" x1="0" y1="0" x2="1" y2="1">
          <stop offset="0.35" stop-color="#000000"/>
          <stop offset="1" stop-color="#6a6a6a"/>
        </linearGradient>
        <linearGradient id="gold-swoosh" x1="0" y1="0" x2="1" y2="0">
          <stop offset="0" stop-color="#c48a2a"/>
          <stop offset="0.45" stop-color="#f6e55e"/>
          <stop offset="1" stop-color="#b8672e"/>
        </linearGradient>
      </defs>
      <path class="header-band" d="M0 0 H905 V181 C600 190 260 240 0 354 Z" fill="url(#header-shade)"/>
      <path class="gold-swoosh" d="M129 318 C350 250 650 205 905 197 V229 C650 226 400 252 129 318 Z" fill="url(#gold-swoosh)"/>
    </svg>

    <div class="brand brand--front">
      <span class="brand__dot"></span>
      <p class="brand__name">Maple Crest<br>Realestate</p>
    </div>

    <div class="person">
      <p class="person__name">NAME XXXXXXX</p>
      <p class="person__title">TITLE XXXXXXXX</p>
    </div>

    <ul class="contact">
      <li class="contact__item">
        <svg class="contact__icon" viewBox="0 0 24 24" aria-hidden="true"><path d="M2 8 C2 4 22 4 22 8 V10 H16 V8 H8 V10 H2 Z M6 11 H18 L20 20 H4 Z" fill="#111"/><circle cx="12" cy="15" r="2.5" fill="#fff"/></svg>
        XXXXXXXXXX
      </li>
      <li class="contact__item">
        <svg class="contact__icon" viewBox="0 0 24 24" aria-hidden="true"><path d="M3 12 L12 4 L21 10 L12 20 Z" fill="#111"/><path d="M3 12 L14 13 L21 10" stroke="#fff" stroke-width="1.5" fill="none"/></svg>
        XXXXXXXXXXXXXXXXXX
      </li>
      <li class="contact__item">
        <svg class="contact__icon" viewBox="0 0 24 24" aria-hidden="true"><g fill="none" stroke="#111" stroke-width="1.6"><circle cx="12" cy="12" r="9"/><ellipse cx="12" cy="12" rx="4" ry="9"/><path d="M3 12 H21 M5 7 H19 M5 17 H19"/></g></svg>
        XXXXXXXXXXXXXXXX
      </li>
    </ul>

    <div class="address">
      <svg class="address__icon" viewBox="0 0 47 46" aria-hidden="true"><path d="M0 16 L23.5 0 L47 16 V46 H33 V24 H14 V46 H0 Z" fill="#111"/></svg>
      <span class="address__rule"></span>
      <div class="address__lines">
        <p>XXXXXXXXXXX</p>
        <p>XXXXXXXXXXXXXXXXXX</p>
      </div>
    </div>
  </section>

  <section class="card card--back" aria-label="Business card back">
    <svg class="card__art" viewBox="0 0 905 543" aria-hidden="true">
      <path class="gloss" d="M0 0 H905 V0 L905 0 C800 100 650 200 476 212 C330 170 160 150 0 145 Z" fill="#ffffff" fill-opacity="0.08"/>
    </svg>
    <div class="brand brand--back">
      <span class="brand__dot"></span>
      <p class="brand__name">Maple Crest<br>Realestate</p>
    </div>
  </section>

</main>
</body>
</html>
```